Fernwick

We require a professional design for a Cosmetic Surgery college. We have just submitted the request for our new logo which will be used on this card. We are the leaders in our field of education in Australia and this should be reflected in the quality of the card. People want to come and study with us because we are so outstanding in the field. Studying with us provides credibility, quality and courage.
Updates

Project Deadline Extended
Reason: Require updated logo to be used in design

Target Market(s)

25 - 40 year old professional women primarily from a medical background wanting to continue study in the cosmetic medical field, western speaking countries. The course average cost is 17k AU for 16 weeks.

Industry/Entity Type

Education

Requirements
Must have
• Must us the logo that is currently under design by this company.
Nice to have
• A medical twist very subtle would be nice possilbly rod of Asclepius.
Should not have
• Should not look old, we are dealing with modern medical concepts.
The logo that is being redesigned 3d silver, the attached logo is the old one.

```html
<!DOCTYPE html>
<html lang="en">
<head>
<meta charset="utf-8">
<title>Fernwick Business Card</title>
<link rel="stylesheet" href="https://fonts.googleapis.com/css2?family=Roboto+Condensed:wght@700&family=Ubuntu:wght@400;500;700&display=swap">
<style>
  :root {
    --teal: #1e6c88;
    --teal-dark: #175a72;
    --ice: #a8cad8;
    --paper: #ffffff;
    --paper-shade: #eceeef;
    --stage: #e4e6e8;
    --rule-grey: #b9bcbf;
  }
  * { box-sizing: border-box; margin: 0; padding: 0; }
  html, body { width: 1200px; height: 900px; overflow: hidden; }
  body {
    background: var(--stage);
    position: relative;
    font-family: "Ubuntu", sans-serif;
  }
  .card {
    position: absolute;
    width: 700px;
    height: 400px;
    background: linear-gradient(135deg, var(--paper) 45%, var(--paper-shade) 100%);
    box-shadow: 0 6px 22px rgba(0,0,0,0.18);
    overflow: hidden;
  }
  .card-front { left: 60px; top: 40px; }
  .card-back { left: 440px; top: 460px; }

  .bottom-band {
    position: absolute; left: 0; right: 0; bottom: 0;
    height: 8px; background: var(--teal);
  }

  /* Front */
  .medical-emblem {
    position: absolute; left: 28px; top: 30px;
    width: 84px; height: 84px;
    background: var(--ice);
    border-radius: 50%;
  }
  .holder-name {
    position: absolute; left: 110px; top: 190px;
    font-family: "Roboto Condensed", sans-serif;
    font-weight: 700;
    font-size: 28px;
    color: var(--teal-dark);
  }
  .divider {
    position: absolute; left: 388px; top: 42px;
    width: 5px; height: 290px;
    background: linear-gradient(to bottom, var(--teal) 0 45%, var(--rule-grey) 45% 100%);
  }
  .contact-list {
    position: absolute; left: 410px; top: 50px;
    list-style: none;
    color: var(--teal-dark);
    font-size: 16px;
    font-weight: 500;
    line-height: 1.05;
  }
  .contact-list li {
    display: flex; align-items: flex-start; gap: 8px;
    margin-bottom: 22px;
  }
  .contact-list svg { flex: none; width: 18px; height: 18px; fill: var(--teal-dark); }
  .social-square {
    flex: none; width: 16px; height: 16px; background: var(--teal-dark); margin-top: 1px;
  }
  .front-brand {
    position: absolute; left: 0; right: 0; bottom: 26px;
    display: flex; justify-content: center; align-items: center; gap: 8px;
  }
  .front-brand .brand-dot {
    width: 30px; height: 30px; border-radius: 50%; background: var(--rule-grey);
  }
  .front-brand .brand-name {
    font-size: 24px; font-weight: 500; letter-spacing: 2px; color: #8a8f93;
  }

  /* Back */
  .back-brand {
    position: absolute; left: 0; right: 0; top: 0; bottom: 8px;
    display: flex; justify-content: center; align-items: center; gap: 18px;
  }
  .back-brand .brand-dot {
    width: 110px; height: 110px; border-radius: 50%; background: var(--teal);
  }
  .back-brand .brand-name {
    font-size: 66px; font-weight: 500; letter-spacing: 3px; color: var(--teal);
  }
</style>
</head>
<body>

<section class="card card-front">
  <div class="medical-emblem" role="img" aria-label="Medical star emblem with staff"></div>
  <h1 class="holder-name">Name Surname</h1>
  <div class="divider"></div>
  <ul class="contact-list">
    <li>
      <svg viewBox="0 0 24 24" aria-hidden="true"><path d="M12 2a7 7 0 0 0-7 7c0 5 7 13 7 13s7-8 7-13a7 7 0 0 0-7-7zm0 9.5A2.5 2.5 0 1 1 12 6.5a2.5 2.5 0 0 1 0 5z"/></svg>
      <span>Level 2, 18 Marlow Lane<br>Harbourview QLD 4290</span>
    </li>
    <li>
      <svg viewBox="0 0 24 24" aria-hidden="true"><path d="M6.6 10.8a15.2 15.2 0 0 0 6.6 6.6l2.2-2.2c.3-.3.7-.4 1-.2 1.1.4 2.3.6 3.6.6.6 0 1 .4 1 1V20c0 .6-.4 1-1 1A17 17 0 0 1 3 4c0-.6.4-1 1-1h3.5c.6 0 1 .4 1 1 0 1.3.2 2.5.6 3.6.1.3 0 .7-.2 1z"/></svg>
      <span>0755008142</span>
    </li>
    <li>
      <svg viewBox="0 0 24 24" aria-hidden="true"><path d="M2 5h20v14H2zm2 2v.5l8 5 8-5V7zm0 2.9V17h16V9.9l-8 5z"/></svg>
      <span>E-mail</span>
    </li>
    <li>
      <svg viewBox="0 0 24 24" aria-hidden="true"><path d="M12 2a10 10 0 1 0 0 20 10 10 0 0 0 0-20zm6.9 9h-3a15 15 0 0 0-1.3-5.6A8 8 0 0 1 18.9 11zM12 4c.9 1.2 1.8 3.6 1.9 7h-3.8c.1-3.4 1-5.8 1.9-7zM9.4 5.4A15 15 0 0 0 8.1 11h-3a8 8 0 0 1 4.3-5.6zM5.1 13h3a15 15 0 0 0 1.3 5.6A8 8 0 0 1 5.1 13zM12 20c-.9-1.2-1.8-3.6-1.9-7h3.8c-.1 3.4-1 5.8-1.9 7zm2.6-1.4a15 15 0 0 0 1.3-5.6h3a8 8 0 0 1-4.3 5.6z"/></svg>
      <span>www.fernwick.com.au</span>
    </li>
    <li>
      <span class="social-square"></span>
      <span>FernwickEdu</span>
    </li>
    <li>
      <span class="social-square"></span>
      <span>FernwickEdu</span>
    </li>
  </ul>
  <div class="front-brand">
    <span class="brand-dot"></span>
    <span class="brand-name">FERNWICK</span>
  </div>
  <div class="bottom-band"></div>
</section>

<section class="card card-back">
  <div class="back-brand">
    <span class="brand-dot"></span>
    <span class="brand-name">FERNWICK</span>
  </div>
  <div class="bottom-band"></div>
</section>

</body>
</html>
```